Valdoria necesita diseños de papeleria como tarjeta de presentacion, hoja membretada, sobres...

La papelería corporativa es para una tienda de moda multimarcas ubicada en Ecuador.
Los diseños tienen que ser de acuerdo a los diseños que adjunto.

```html
<!DOCTYPE html>
<html lang="es">
<head>
<meta charset="utf-8">
<title>Valdoria · Papelería corporativa</title>
<link rel="stylesheet" href="https://fonts.googleapis.com/css2?family=Montserrat:wght@400;500&display=swap">
<style>
  :root {
    --backdrop: #e3e3e3;
    --ink: #000000;
    --paper: #ffffff;
    --accent: #e3241b;
    --muted: #cfcfcf;
    --motif: linear-gradient(135deg, #f2f2f2 0%, #d9d9d9 45%, #e3241b 100%);
  }
  * { margin: 0; padding: 0; box-sizing: border-box; }
  html, body { width: 1200px; height: 893px; overflow: hidden; }
  body {
    position: relative;
    background: var(--backdrop);
    font-family: "Montserrat", sans-serif;
    color: var(--paper);
  }

  .wordmark { display: flex; flex-direction: column; align-items: center; width: max-content; }
  .wordmark__name {
    font-weight: 500;
    letter-spacing: 0.22em;
    text-transform: uppercase;
    line-height: 1;
    margin-right: -0.22em;
  }
  .wordmark__tagline {
    font-weight: 400;
    letter-spacing: 0.28em;
    text-transform: uppercase;
    line-height: 1;
    margin-right: -0.28em;
  }

  .brand-motif {
    position: absolute;
    background: var(--motif);
  }

  /* Letterhead */
  .letterhead {
    position: absolute;
    left: 203px; top: 147px;
    width: 444px; height: 625px;
    background: var(--paper);
  }
  .letterhead__band {
    position: absolute; left: 0; top: 0;
    width: 102px; height: 100%;
    background: var(--ink);
  }
  .letterhead .wordmark { position: absolute; left: 11px; top: 24px; }
  .letterhead .wordmark__name { font-size: 10px; }
  .letterhead .wordmark__tagline { font-size: 4.2px; margin-top: 3px; }
  .letterhead__contact {
    position: absolute; left: 11px; top: 52px;
    font-size: 4.4px; line-height: 1.35;
  }
  .letterhead__contact p + p { margin-top: 4px; }
  .letterhead .brand-motif { left: 0; top: 486px; width: 102px; height: 139px; }

  /* Business cards */
  .card {
    position: absolute;
    top: 321px;
    height: 106px;
    background: var(--ink);
    overflow: hidden;
  }
  .card--front { left: 692px; width: 172px; }
  .card--back { left: 882px; width: 171px; }
  .card--front .wordmark { position: absolute; left: 12px; top: 14px; }
  .card--front .wordmark__name { font-size: 9.5px; }
  .card--front .wordmark__tagline { font-size: 4px; margin-top: 2px; }
  .card__rule {
    position: absolute; left: 13px; top: 76px;
    width: 1px; height: 21px;
    background: var(--accent);
  }
  .card__contact {
    position: absolute; left: 20px; top: 75px;
    font-size: 3.2px; line-height: 1.75;
    color: var(--muted);
  }
  .card--back .brand-motif { left: 0; top: 0; width: 85px; height: 106px; }

  /* Envelope */
  .envelope {
    position: absolute;
    left: 613px; top: 467px;
    width: 441px; height: 220px;
    background: var(--ink);
    overflow: hidden;
  }
  .envelope .wordmark { position: absolute; right: 27px; top: 22px; }
  .envelope .wordmark__name { font-size: 15px; }
  .envelope .wordmark__tagline { font-size: 6.2px; margin-top: 4px; }
  .envelope .brand-motif { left: 0; top: 0; width: 185px; height: 220px; }
</style>
</head>
<body>

  <section class="letterhead" aria-label="Hoja membretada">
    <div class="letterhead__band">
      <div class="wordmark">
        <span class="wordmark__name">Valdoria</span>
        <span class="wordmark__tagline">Moda &amp; Lenceria</span>
      </div>
      <div class="letterhead__contact">
        <p>Av. Las Palmas, Puerto Lindo<br>Ecuador</p>
        <p>(07) 555-0142<br>www.valdoria.com</p>
      </div>
      <div class="brand-motif" role="img" aria-label="Motivo gráfico de la marca con franjas diagonales blanca y roja"></div>
    </div>
  </section>

  <section class="card card--front" aria-label="Tarjeta de presentación, anverso">
    <div class="wordmark">
      <span class="wordmark__name">Valdoria</span>
      <span class="wordmark__tagline">Moda &amp; Lenceria</span>
    </div>
    <span class="card__rule"></span>
    <div class="card__contact">
      <p>Av. Las Palmas, Puerto Lindo Ecuador</p>
      <p>(07) 555-0142</p>
      <p>info@valdoria.com</p>
      <p>www.valdoria.com</p>
    </div>
  </section>

  <section class="card card--back" aria-label="Tarjeta de presentación, reverso">
    <div class="brand-motif" role="img" aria-label="Motivo gráfico de la marca con franjas diagonales blanca y roja"></div>
  </section>

  <section class="envelope" aria-label="Sobre">
    <div class="brand-motif" role="img" aria-label="Motivo gráfico de la marca con franjas diagonales blanca y roja"></div>
    <div class="wordmark">
      <span class="wordmark__name">Valdoria</span>
      <span class="wordmark__tagline">Moda &amp; Lenceria</span>
    </div>
  </section>

</body>
</html>
```